Template design for organic gardening site for ShopTrellis platform

We need a template design for our new 'Fern Patch Naturals' shoptrellis site. Fern Patch Naturals specialises in organic nutrients for gardening plus all equipment needed to grow.
Domain name will be www.fernpatchnaturals.co.uk
Colours used should include logo colours, see attached image. Other colours to compliment the greens and lift the feel of the site could be yellow or orange.
Home page design should include, but not limited to the following:
Interactive banner carousel space
A smaller banner advertising space
Featured products
New products
Sale products feature/link
Articles links/feature
+ all standard shoptrellis features such as menus, etc
The site will be selling products (these are nutrients) such as:
Mistravelon
Heronwing soil remedy
Verdolux
Root pods
Leaf triumph
Stem wonder
Tiv
Humus prime
Terravine
+ more products and brands
Site layouts we like include:
www.fernpatchaquatics.co.uk ... A bit old fashioned but cool
www.larkplots.co.uk ... Nice but too compact
www.humusprime.com ... Has a nice top half
www.sponsorasprout.org.uk ... Nice colours and header
www.pennickbeds.co.uk ... nice layout, but needs image carousel
www.wrenseed.co.uk ... Nice background and colours
www.tulipa.co.uk ... Nice colours and layout
www.marcusbellowayplantcraft.com ... Nice layout and header
www.sprouteo.co.uk ... Cool colours and shop pages layout is nice
www.aquafarmix.co.uk ... One of the best layouts
The site should feel clean, modern and elegant.
Reason: The brief has been revised slightly and some designs we have received need to be tweeked.
Reason: We would like to see a few more designs that are on brief
Target Market(s)
Indoor and outdoor organic gardeners
Look and feel

```html
<!DOCTYPE html>
<html lang="en">
<head>
<meta charset="utf-8">
<title>Fern Patch Naturals</title>
<link href="https://fonts.googleapis.com/css2?family=Oswald:wght@300;400&family=Open+Sans:wght@400;600&display=swap" rel="stylesheet">
<style>
:root{
  --green:#4b7d3b;
  --green-dark:#2f5e1c;
  --green-mid:#5f9448;
  --green-light:#8ab86b;
  --orange:#f28c1c;
  --page:#ececec;
  --panel:#ffffff;
  --text:#555555;
  --heading:#3d6e2c;
  --line:#e2e2e2;
  --grey-icon:#c9c9c9;
}
*{box-sizing:border-box;margin:0;padding:0}
html,body{width:1200px;height:2507px;overflow:hidden}
body{position:relative;background:var(--page);font-family:"Open Sans",Arial,sans-serif;color:var(--text)}
.abs{position:absolute}
.panel{left:127px;top:0;width:946px;height:2202px;background:var(--panel)}
.nav{left:127px;top:0;width:946px;height:52px;background:var(--green);display:flex;align-items:stretch}
.nav a{font-family:"Oswald",sans-serif;font-weight:400;font-size:16px;color:#fff;text-decoration:none;display:flex;align-items:center;padding:0 26px}
.nav a.active{background:#fff;color:#333}
.nav .search{margin-left:auto;display:flex;align-items:center;gap:12px;padding-right:22px;color:#e8f0e2;font-size:14px;font-style:italic}
.logo{left:150px;top:78px;display:flex;align-items:center;gap:10px}
.logo .mark{width:44px;height:44px;background:var(--green)}
.logo .name{font-family:"Oswald",sans-serif;font-weight:400;font-size:24px;line-height:24px;color:var(--green);text-transform:uppercase;width:150px}
.phone{left:769px;top:88px;font-family:"Oswald",sans-serif;font-weight:300;font-size:24px;color:var(--orange);display:flex;align-items:center;gap:8px}
.social{display:flex;gap:7px}
.social span{width:24px;height:24px;background:var(--grey-icon);display:block}
.banner{left:150px;top:155px;width:899px;height:373px;background:linear-gradient(100deg,#5e9246 0%,#4f8538 55%,#6da052 100%);overflow:hidden}
.banner h1{position:absolute;left:38px;top:105px;font-family:"Oswald",sans-serif;font-weight:400;font-size:33px;color:#fff;text-transform:uppercase;letter-spacing:-0.5px}
.banner p{position:absolute;left:38px;top:156px;width:410px;font-size:19px;line-height:26px;color:#fff}
.banner .photo{position:absolute;left:470px;top:55px;width:430px;height:290px;background:radial-gradient(ellipse at 55% 50%,#c7d79a 0%,#8fa863 45%,rgba(90,140,70,0) 72%)}
.banner .dots{position:absolute;right:22px;top:23px;display:flex;gap:6px}
.banner .dots i{width:9px;height:9px;background:#b5cfa3;transform:rotate(45deg);display:block}
.banner .dots i.on{background:#fff}
.cta{position:absolute;left:40px;top:301px;width:201px;height:42px;font-family:"Oswald",sans-serif;font-weight:300;font-size:17px;color:#333;display:flex;align-items:center}
.cta span{position:relative;left:25px}
.cta svg{position:absolute;left:0;top:0}
.heading{font-family:"Oswald",sans-serif;font-weight:300;font-size:23px;color:var(--heading)}
.dots-rule{height:6px;background:radial-gradient(circle,#d3d3d3 1.4px,transparent 1.6px) 0 0/6px 6px repeat-x}
.about p{font-size:15px;line-height:22.5px;color:#555}
.more{font-size:12px;color:#444;padding-bottom:3px;border-bottom:2px solid #ddd;display:inline-block}
.side-head{background:var(--green);color:#fff;font-family:"Oswald",sans-serif;font-size:19px;font-weight:400;padding-left:24px;display:flex;align-items:center}
.box{border:1px solid var(--line);border-top:none}
.cats li{list-style:none;display:flex;gap:12px;padding:9px 10px 9px 22px;border-bottom:1px solid var(--line);font-size:15px;line-height:18px;color:#555;min-height:37.6px}
.cats li:last-child{border-bottom:none}
.cats li::before{content:"";flex:none;width:14px;height:14px;border-radius:50%;background:#e6e6e6;margin-top:2px}
.card{width:207px;height:346px;border:1px solid var(--line);position:absolute}
.card .img{position:absolute;left:22px;top:14px;width:163px;height:142px}
.card h3{position:absolute;left:27px;top:176px;font-family:"Oswald",sans-serif;font-weight:300;font-size:23px;color:#555}
.card p{position:absolute;left:27px;top:214px;width:165px;font-size:12.5px;line-height:15px;color:#666}
.card .price{position:absolute;left:27px;top:252px;font-family:"Oswald",sans-serif;font-weight:400;font-size:24px;color:var(--green)}
.card .more{position:absolute;left:27px;top:303px;font-size:12px}
.img-basket{background:radial-gradient(circle at 50% 55%,#c9813a 0%,#9b6b3a 40%,rgba(255,255,255,0) 70%)}
.img-soap{background:radial-gradient(ellipse at 50% 55%,#8fb05c 0%,#d9d3a2 45%,rgba(255,255,255,0) 70%)}
.img-bottles{background:radial-gradient(ellipse at 50% 55%,#e6c07a 0%,#b58755 40%,rgba(255,255,255,0) 70%)}
.img-tube{background:radial-gradient(ellipse at 50% 55%,#9cb24a 0%,#5f7526 35%,rgba(255,255,255,0) 62%)}
.article-img{width:180px;height:102px}
.date{position:absolute;left:0;bottom:0;width:58px;height:38px;background:#fff;display:flex;align-items:center;gap:3px;padding-left:6px}
.date b{font-family:"Oswald",sans-serif;font-weight:400;font-size:23px;color:#555}
.date small{font-size:10px;line-height:10px;color:#777}
.article p{font-size:12.5px;line-height:15px;color:#555;width:185px}
.callbar{left:353px;top:2181px;width:494px;height:47px;background:#fff;font-family:"Oswald",sans-serif;font-weight:300;font-size:33px;color:var(--green-dark);display:flex;align-items:center;justify-content:center;gap:12px}
.footer{left:0;top:2202px;width:1200px;height:305px;background:linear-gradient(180deg,#2f6018 0%,#3d7524 60%,#4e8a34 100%)}
.fhead{font-family:"Oswald",sans-serif;font-weight:300;font-size:18px;color:#fff;text-transform:uppercase}
.flist li{list-style:none;font-size:12.5px;line-height:22.5px;color:#fff}
.fdiv{width:1px;background:rgba(255,255,255,0.2)}
.ftext{font-size:12.5px;line-height:20px;color:#fff}
</style>
</head>
<body>
<div class="abs panel"></div>

<nav class="abs nav">
  <a>HOME</a><a class="active">ABOUT US</a><a>OUR PRODUCTS</a><a>OUR SERVICES</a><a>REVIEWS</a><a>CONTACT US</a>
  <div class="search">Search...
    <svg width="16" height="16" viewBox="0 0 16 16"><circle cx="6.5" cy="6.5" r="4.5" fill="none" stroke="#fff" stroke-width="2"/><line x1="10" y1="10" x2="14" y2="14" stroke="#fff" stroke-width="2.5"/></svg>
  </div>
</nav>

<div class="abs logo"><span class="mark"></span><span class="name">Fern Patch Naturals</span></div>

<div class="abs phone">
  <svg width="14" height="22" viewBox="0 0 14 22"><rect x="1.5" y="1.5" width="11" height="19" rx="2" fill="none" stroke="#f28c1c" stroke-width="2.5"/><line x1="5" y1="17" x2="9" y2="17" stroke="#f28c1c" stroke-width="2"/></svg>
  002 456 7100
</div>
<div class="abs social" style="left:929px;top:92px"><span></span><span></span><span></span><span></span></div>

<section class="abs banner">
  <div class="photo" role="img" aria-label="Stacked organic soap bars with a certified badge"></div>
  <div class="dots"><i></i><i class="on"></i><i></i><i></i></div>
  <h1>Lorem Organic Product Title</h1>
  <p>Nulla id mollis nisi sagittis dolor. Proin purus, laoreet libero sit pellentesque nec.</p>
  <div class="cta">
    <svg width="201" height="42" viewBox="0 0 201 42"><path d="M0 0H201L188 21L201 42H0Z" fill="#fff"/><circle cx="153" cy="21" r="8" fill="#4b7d3b"/><path d="M149 21l3 3 5-6" stroke="#fff" stroke-width="2" fill="none"/></svg>
    <span>CALL TO ACTION</span>
  </div>
</section>

<section class="about">
  <h2 class="abs heading" style="left:150px;top:574px">About Fern Patch Naturals</h2>
  <div class="abs dots-rule" style="left:150px;top:617px;width:899px"></div>
  <p class="abs" style="left:150px;top:636px;width:899px">Nulla id mollis nisi,vel sagittis dolor. Pellentesque orci. Donec ac pharetra magna. Duis vitae mauris a turpis consectetur vulputate at et libero. Cras ut . Morbi semper, metus ac cursus ullamcorper, sem est tempor arcu, quis blandit massa nisl sed tortor. Feugiat in nisi eget ullamcorper. Sed scelerisque interdum ligula</p>
  <span class="abs more" style="left:988px;top:726px">Learn More</span>
</section>

<aside>
  <div class="abs side-head" style="left:150px;top:772px;width:224px;height:50px">Categories</div>
  <ul class="abs box cats" style="left:150px;top:822px;width:224px;height:443px;padding-top:4px">
    <li>Mistravelon</li><li>Heronwing soil remedy</li><li>Verdolux</li><li>Root pods</li><li>Leaf triumph</li><li>Stem wonder</li><li>Tiv</li><li>Humus prime</li><li>Terravine</li><li>More products and Brands</li>
  </ul>
  <div class="abs" role="img" aria-label="Advertisement for evening wear shirts" style="left:150px;top:1312px;width:224px;height:187px;background:linear-gradient(135deg,#3a1f3a 0%,#7b3a6a 50%,#2a2a4a 100%)"></div>

  <div class="abs side-head" style="left:150px;top:1541px;width:224px;height:48px">Articles</div>
  <div class="abs box" style="left:150px;top:1589px;width:224px;height:445px"></div>
  <div class="abs article" style="left:169px;top:1616px">
    <div class="article-img" role="img" aria-label="Green bamboo forest" style="position:relative;background:linear-gradient(90deg,#3f7d22,#8cc04a,#4b8a2a)">
      <div class="date"><b>14</b><small>DEC<br>2015</small></div>
    </div>
    <p style="margin-top:20px">Nulla id mollis nisi sagittis dolor. Proin purus , laoreet nec. Donec ac</p>
  </div>
  <div class="abs article" style="left:169px;top:1805px">
    <div class="article-img" role="img" aria-label="Pale green flowers on a pink background" style="position:relative;background:linear-gradient(120deg,#c9d98f,#e0e6b8 50%,#d49ab0)">
      <div class="date"><b>14</b><small>DEC<br>2015</small></div>
    </div>
    <p style="margin-top:20px">Nulla id mollis nisi sagittis dolor. Proin purus , laoreet nec. Donec ac</p>
  </div>
  <span class="abs more" style="left:174px;top:1990px">Learn More</span>
</aside>

<main>
  <h2 class="abs heading" style="left:399px;top:768px">Featured Products</h2>
  <div class="abs dots-rule" style="left:399px;top:816px;width:650px"></div>

  <div class="card" style="left:399px;top:847px">
    <div class="img img-basket" role="img" aria-label="Basket of fresh vegetables and produce"></div>
    <h3>Product Title</h3><p>Welcome text nulla id sagittis dolor. Proin enim</p><div class="price">£79.95</div><span class="more">Learn More</span>
  </div>
  <div class="card" style="left:621px;top:847px">
    <div class="img img-soap" role="img" aria-label="Organic soap bars"></div>
    <h3>Product Title</h3><p>Welcome text nulla id sagittis dolor. Proin enim</p><div class="price">£79.95</div><span class="more">Learn More</span>
  </div>
  <div class="card" style="left:842px;top:847px">
    <div class="img img-bottles" role="img" aria-label="Skincare bottles and jars"></div>
    <h3>Product Title</h3><p>Welcome text nulla id sagittis dolor. Proin enim</p><div class="price">£79.95</div><span class="more">Learn More</span>
  </div>

  <div class="abs" role="img" aria-label="Advertising banner for an education charity" style="left:438px;top:1240px;width:546px;height:67px;background:linear-gradient(90deg,#8cc43f 0%,#8cc43f 18%,#e8d2b8 18%,#d9b99a 50%,#1a72b8 50%,#1a72b8 100%)"></div>

  <h2 class="abs heading" style="left:399px;top:1350px">New Products</h2>
  <div class="abs dots-rule" style="left:399px;top:1397px;width:650px"></div>

  <div class="card" style="left:399px;top:1439px">
    <div class="img img-bottles" role="img" aria-label="Skincare bottles and jars"></div>
    <h3>Product Title</h3><p>Welcome text nulla id sagittis dolor. Proin enim</p><div class="price">£79.95</div><span class="more">Learn More</span>
  </div>
  <div class="card" style="left:621px;top:1439px">
    <div class="img img-tube" role="img" aria-label="Green shampoo bottle"></div>
    <h3>Product Title</h3><p>Welcome text nulla id sagittis dolor. Proin enim</p><div class="price">£79.95</div><span class="more">Learn More</span>
  </div>
  <div class="card" style="left:842px;top:1439px">
    <div class="img img-basket" role="img" aria-label="Basket of fresh vegetables and produce"></div>
    <h3>Product Title</h3><p>Welcome text nulla id sagittis dolor. Proin enim</p><div class="price">£79.95</div><span class="more">Learn More</span>
  </div>

  <div class="abs" role="img" aria-label="Four white lotion bottles with green caps and a starfish" style="left:401px;top:1838px;width:334px;height:276px;background:radial-gradient(ellipse at 50% 50%,#e9eef0 0%,#cfd9dc 35%,#a7cf6a 50%,rgba(255,255,255,0) 72%)"></div>
  <h2 class="abs heading" style="left:745px;top:1856px;font-size:33px;color:#555">Sale Products</h2>
  <div class="abs dots-rule" style="left:745px;top:1909px;width:255px"></div>
  <p class="abs" style="left:745px;top:1930px;width:265px;font-size:14px;line-height:20px;color:#555">Nulla id mollis nisi,vel sagittis dolor. Proin purus enim, et libero sit amet laoreet et libero sit amet. nec. Donec ac pharetra magna.</p>
  <div class="abs" style="left:745px;top:2016px;font-family:'Oswald',sans-serif;font-weight:300;font-size:33px;color:var(--green)">£79.95</div>
  <span class="abs more" style="left:867px;top:2030px">Learn More</span>
</main>

<footer class="abs footer">
  <div class="abs" style="left:149px;top:70px"><div class="fhead">Quick Links</div>
    <ul class="flist" style="margin-top:14px"><li>Home</li><li>About Us</li><li>Our Products</li><li>Our Services</li><li>Reviews</li><li>Contact Us</li></ul></div>
  <div class="abs fdiv" style="left:272px;top:70px;height:210px"></div>
  <div class="abs" style="left:317px;top:70px"><div class="fhead">Categoreis</div>
    <div style="display:flex;gap:28px;margin-top:14px">
      <ul class="flist" style="width:108px"><li>Mistravelon</li><li style="line-height:18px;margin:2px 0 4px">Heronwing soil remedy</li><li>Verdolux</li><li>Root pods</li><li>Leaf triumph</li></ul>
      <ul class="flist" style="width:118px"><li>Stem wonder</li><li>Tiv</li><li>Humus prime</li><li>Terravine</li><li style="line-height:22px">More products and Brands</li></ul>
    </div></div>
  <div class="abs fdiv" style="left:603px;top:70px;height:210px"></div>
  <div class="abs" style="left:660px;top:70px"><div class="fhead">Contact Us</div>
    <p class="ftext" style="margin-top:14px;width:150px">Head Office :<br>Fern Patch Naturals LLC 482 Marlow Ave, XXX Floor, Orchard Road, California 90412</p></div>
  <div class="abs fdiv" style="left:844px;top:70px;height:210px"></div>
  <div class="abs" style="left:872px;top:66px">
    <p class="ftext" style="width:190px">Copyright fernpatchnaturals.com 2015. All right reserved</p>
    <div class="social" style="margin-top:14px"><span style="background:#7c9c6c"></span><span style="background:#7c9c6c"></span><span style="background:#7c9c6c"></span><span style="background:#7c9c6c"></span></div>
  </div>
</footer>

<div class="abs callbar">
  <svg width="14" height="24" viewBox="0 0 14 24"><rect x="1.5" y="1.5" width="11" height="21" rx="2" fill="none" stroke="#2f5e1c" stroke-width="2.5"/><line x1="5" y1="18.5" x2="9" y2="18.5" stroke="#2f5e1c" stroke-width="2"/></svg>
  <span>CALL US TODAY&nbsp;&nbsp;&nbsp;002 456 7100</span>
</div>
</body>
</html>
```